Design a CD Cover For Baby Music and Lullabies To Appear on Tunvale Store etc.

Please read this brief before you design. Otherwise you will be wasting your time.

I need a cd cover for music albums which will appear on streaming sites such as Tunvale Store Melodrift, Vimtro etc. for the brand Snug Cradle Tunes. The thumbnails are quite small so the text needs to be quite large.

I need a design if possible, in which I can simply alter the title of the album and the baby picture so that each album has a different cover but works with the branding.

You can check out the Snug Cradle Tunes on the Tunvale store.
https://play.melodriftaudio.net/artist/8kQ3xTnRwLpV27hYbMdZc4

I made those covers and I really don't like them at all! As you can tell I am not a graphic designer. Ha.

Please help me with a modern, eye catching and cute design that will work across the brand now and in the future. The SCT logo and the name Snug Cradle Tunes is the only thing that needs to be used somewhere in the design.

Please use the title

Gentle Static Hums For Nap Time Series A

for this first album.
(White noise sounds are hair dryers, vacuum cleaners, fans, wind, rain, the sea, white noise, pink noise, brown noise etc. )

Here is an example of album covers which are coherent. A style like this without the over the top text would be good. But don't copy these!
https://play.melodriftaudio.net/artist/9TqWmLx5Rb2Hn7KcVpYe1z

Target Market(s)

Parents of babies.

Font styles to use
Serif
Sans Serif

Colors

Designer to choose colors to be used in the design.

Requirements
Must have
• Large font so it can been seen in the melodrift thumbnail. A photo of a baby. Please take a look at the melodrift and tunvale stores. The Snug Cradle Tunes logo.
• Album Title
• Gentle Static Hums For Nap Time Series A

```html
<!DOCTYPE html>
<html lang="en">
<head>
<meta charset="utf-8">
<title>Gentle Static Hums For Nap Time – Series A</title>
<link rel="stylesheet" href="https://fonts.googleapis.com/css2?family=Jost:wght@300;400&display=swap">
<style>
  :root {
    --stage: #4a4a4a;
    --cover-light: #d9dbda;
    --cover-mid: #b9bcbb;
    --cover-edge: #8e9292;
    --water-deep: #3d4a52;
    --water-mid: #7c878c;
    --ink: #23201d;
    --brand-dot: #3a63b3;
  }
  * { margin: 0; padding: 0; box-sizing: border-box; }
  html, body {
    width: 1200px;
    height: 960px;
    overflow: hidden;
    background: var(--stage);
  }
  .album-cover {
    position: absolute;
    left: 160px;
    top: 40px;
    width: 880px;
    height: 880px;
    overflow: hidden;
    background: radial-gradient(ellipse at 50% 40%, var(--cover-light) 0%, var(--cover-mid) 65%, var(--cover-edge) 100%);
    font-family: "Jost", "Futura", sans-serif;
    color: var(--ink);
  }
  .splash-photo {
    position: absolute;
    left: 190px;
    top: 430px;
    width: 500px;
    height: 420px;
    border-radius: 50%;
    background: radial-gradient(ellipse at 50% 42%, var(--water-deep) 0%, var(--water-mid) 45%, rgba(185,188,187,0) 72%);
  }
  .album-title {
    position: absolute;
    left: 0;
    top: 0;
    width: 100%;
    text-align: center;
    font-weight: 300;
    text-transform: uppercase;
    line-height: 1;
  }
  .title-line { position: absolute; left: 0; width: 100%; white-space: nowrap; }
  .title-line--lead { top: 82px; font-size: 90px; letter-spacing: 1px; }
  .title-line--middle { top: 186px; font-size: 74px; }
  .title-line--main { top: 271px; font-size: 100px; font-weight: 400; }
  .title-line--series { top: 376px; font-size: 38px; letter-spacing: 9px; }
  .brand-mark {
    position: absolute;
    left: 0;
    top: 760px;
    width: 100%;
    display: flex;
    justify-content: center;
    align-items: center;
    gap: 14px;
  }
  .brand-dot {
    width: 34px;
    height: 34px;
    border-radius: 50%;
    background: var(--brand-dot);
  }
  .brand-name {
    font-size: 34px;
    font-weight: 400;
    letter-spacing: 2px;
    color: var(--ink);
  }
</style>
</head>
<body>
  <main class="album-cover">
    <div class="splash-photo" role="img" aria-label="Close-up photograph of a water drop splashing into a crown shape"></div>
    <h1 class="album-title">
      <span class="title-line title-line--lead">Gentle Static</span>
      <span class="title-line title-line--middle">Hums For</span>
      <span class="title-line title-line--main">Nap Time</span>
      <span class="title-line title-line--series">Series A</span>
    </h1>
    <div class="brand-mark">
      <span class="brand-dot"></span>
      <span class="brand-name">Snug Cradle Tunes</span>
    </div>
  </main>
</body>
</html>
```